Investor Presentation

We have a deck that is mostly finished that needs to be properly formatted and cleaned up. The presentation is for an investment in a financial firm. So the design we are looking for is very professional and minimalistic. A very clean look with conservative color schemes and fonts. The designer can leverage our existing logos, background, etc.

The final design files should have full editing functionality.

Target Market(s)

Sophisticated institutional investors

Industry/Entity Type

Conservative

Requirements
Nice to have
• Cleaned up / formatted tables from the attached files to add to the presentation.

```html
<!DOCTYPE html>
<html lang="en">
<head>
<meta charset="utf-8">
<title>Graph data Heading</title>
<link href="https://fonts.googleapis.com/css2?family=Roboto:wght@400;500;700&family=Ubuntu:wght@400;500&display=swap" rel="stylesheet">
<style>
  :root {
    --teal-dark: #03777a;
    --teal-footer: #3a96a0;
    --teal-text: #0e7d80;
    --blue-deep: #1e8db5;
    --blue-light: #6fd2f5;
    --mint: #1bbfa5;
    --body-text: #555b5e;
    --white: #ffffff;
  }
  * { margin: 0; padding: 0; box-sizing: border-box; }
  html, body { width: 1200px; height: 900px; overflow: hidden; background: var(--white); }
  .slide { position: relative; width: 1200px; height: 900px; font-family: "Roboto", sans-serif; }

  .slide-header {
    position: absolute; left: 0; top: 0; width: 1200px; height: 99px;
    background: var(--teal-dark);
    display: flex; align-items: center; justify-content: space-between;
    padding: 0 18px 0 30px;
  }
  .slide-title { font-family: "Ubuntu", sans-serif; font-weight: 500; font-size: 41px; color: var(--white); }
  .brand { display: flex; align-items: center; gap: 12px; font-family: "Ubuntu", sans-serif; font-size: 24px; color: var(--white); }
  .brand-dot { width: 30px; height: 30px; border-radius: 50%; background: var(--white); }

  .section-title {
    position: absolute; left: 52px; top: 164px;
    display: flex; align-items: center; gap: 16px;
    font-weight: 700; font-size: 24px; color: var(--teal-text);
  }
  .section-marker { width: 20px; height: 20px; background: var(--teal-text); }

  .feature { position: absolute; display: flex; align-items: flex-start; }
  .feature-icon {
    position: absolute; width: 92px; height: 92px; border-radius: 50%;
    display: flex; align-items: center; justify-content: center;
  }
  .feature-icon svg { width: 40px; height: 40px; }
  .icon-deep { background: var(--blue-deep); }
  .icon-light { background: var(--blue-light); }
  .icon-mint { background: var(--mint); }
  .feature-body { position: absolute; width: 370px; }
  .feature-heading { font-weight: 700; font-size: 21px; line-height: 26px; margin-bottom: 6px; }
  .heading-deep { color: var(--teal-text); }
  .heading-light { color: var(--blue-light); }
  .heading-mint { color: var(--mint); }
  .feature-text { font-size: 17.5px; line-height: 24px; color: var(--body-text); }

  .slide-footer {
    position: absolute; left: 0; top: 856px; width: 1200px; height: 44px;
    background: var(--teal-footer);
    font-family: "Ubuntu", sans-serif; font-size: 19px; color: var(--white);
    display: flex; align-items: center; padding-left: 12px;
  }
</style>
</head>
<body>
<div class="slide">
  <header class="slide-header">
    <h1 class="slide-title">Graph data Heading</h1>
    <div class="brand"><span class="brand-dot"></span><span>Harbor Ridge Capital, LLC</span></div>
  </header>

  <h2 class="section-title"><span class="section-marker"></span>Bullet Title Heading Here Bullet Title Heading Here</h2>

  <!-- left column -->
  <div class="feature-icon icon-deep" style="left:104px;top:294px;">
    <svg viewBox="0 0 40 40"><circle cx="20" cy="20" r="15" fill="#fff"/><path d="M20 20 L20 5 M20 20 L33 27 M20 20 L9 31" stroke="#1e8db5" stroke-width="2.5" fill="none"/></svg>
  </div>
  <div class="feature-body" style="left:211px;top:302px;">
    <h3 class="feature-heading heading-deep">Subtext here</h3>
    <p class="feature-text">Contrary to popular belief, Lorem Ipsum is not simply random text. It has roots in a piece of classical Latin literature from 45 BC.</p>
  </div>

  <div class="feature-icon icon-light" style="left:101px;top:451px;">
    <svg viewBox="0 0 40 40"><rect x="6" y="8" width="28" height="20" rx="2" fill="#fff"/><rect x="11" y="13" width="14" height="3" fill="#6fd2f5"/><rect x="11" y="19" width="9" height="3" fill="#6fd2f5"/><rect x="14" y="30" width="12" height="3" fill="#fff"/></svg>
  </div>
  <div class="feature-body" style="left:211px;top:455px;">
    <h3 class="feature-heading heading-light">Subtext here</h3>
    <p class="feature-text">Contrary to popular belief, Lorem Ipsum is not simply random text. It has roots in a piece of classical Latin literature from 45 BC.</p>
  </div>

  <div class="feature-icon icon-mint" style="left:101px;top:647px;">
    <svg viewBox="0 0 40 40"><path d="M20 5 L24.4 14.2 L34.5 15.4 L27 22.3 L29 32.3 L20 27.3 L11 32.3 L13 22.3 L5.5 15.4 L15.6 14.2 Z" fill="none" stroke="#fff" stroke-width="2.2" stroke-linejoin="round"/></svg>
  </div>
  <div class="feature-body" style="left:211px;top:636px;">
    <h3 class="feature-heading heading-mint">Subtext here</h3>
    <p class="feature-text">Contrary to popular belief, Lorem Ipsum is not simply random text. It has roots in a piece of classical Latin literature from 45 BC.</p>
  </div>

  <!-- right column -->
  <div class="feature-icon icon-deep" style="left:629px;top:294px;">
    <svg viewBox="0 0 40 40"><circle cx="20" cy="20" r="14" fill="none" stroke="#fff" stroke-width="3.5"/><path d="M20 12 L20 21 L26 24" stroke="#fff" stroke-width="3" fill="none" stroke-linecap="round"/></svg>
  </div>
  <div class="feature-body" style="left:753px;top:302px;">
    <h3 class="feature-heading heading-deep">Subtext here</h3>
    <p class="feature-text">Contrary to popular belief, Lorem Ipsum is not simply random text. It has roots in a piece of classical Latin literature from 45 BC.</p>
  </div>

  <div class="feature-icon icon-light" style="left:631px;top:453px;">
    <svg viewBox="0 0 40 40"><rect x="7" y="11" width="26" height="18" rx="2" fill="#fff"/><path d="M7 12 L20 21 L33 12" stroke="#6fd2f5" stroke-width="2" fill="none"/></svg>
  </div>
  <div class="feature-body" style="left:753px;top:455px;">
    <h3 class="feature-heading heading-light">Subtext here</h3>
    <p class="feature-text">Contrary to popular belief, Lorem Ipsum is not simply random text. It has roots in a piece of classical Latin literature from 45 BC.</p>
  </div>

  <div class="feature-icon icon-mint" style="left:626px;top:647px;">
    <svg viewBox="0 0 40 40"><path d="M5 12 L27 12 L35 20 L27 28 L5 28 Z" fill="none" stroke="#fff" stroke-width="2.2" stroke-linejoin="round"/></svg>
  </div>
  <div class="feature-body" style="left:753px;top:636px;">
    <h3 class="feature-heading heading-mint">Subtext here</h3>
    <p class="feature-text">Contrary to popular belief, Lorem Ipsum is not simply random text. It has roots in a piece of classical Latin literature from 45 BC.</p>
  </div>

  <footer class="slide-footer">Copyright text here</footer>
</div>
</body>
</html>
```